Vr holdings enterprise pty ltd

2 sided card black and red with white
Very professional and elegant

Target Market(s)

Construction and Development

Industry/Entity Type

Construction and development

Contact Information for Business Card

One side black, one side red/or white business logo in top corner, email: morgan@vrholdingsgroup.example

Requirements
Should not have
• Blue

```html
<!DOCTYPE html>
<html lang="en">
<head>
<meta charset="utf-8">
<title>VR Holdings – Business Card</title>
<link rel="stylesheet" href="https://fonts.googleapis.com/css2?family=Montserrat:wght@600;700&family=Arimo:wght@400&display=swap">
<style>
  :root {
    --backdrop: #3b3b3b;
    --card: #000000;
    --accent: #e8391f;
    --ink: #ffffff;
    --rule: #2a2a2a;
  }
  * { box-sizing: border-box; margin: 0; padding: 0; }
  html, body {
    width: 1093px;
    height: 1200px;
    overflow: hidden;
    background: var(--backdrop);
  }
  .card {
    position: absolute;
    left: 264px;
    width: 580px;
    height: 356px;
    background: var(--card);
    color: var(--ink);
    font-family: "Arimo", Arial, sans-serif;
  }
  .card--front { top: 226px; }
  .card--back { top: 620px; }
  .card__band {
    position: absolute;
    left: 0; right: 0; bottom: 0;
    height: 7px;
    background: var(--accent);
  }
  .brand {
    position: absolute;
    display: flex;
    align-items: baseline;
    gap: 5px;
    font-family: "Montserrat", Arial, sans-serif;
    font-weight: 700;
    color: var(--ink);
    letter-spacing: 0.5px;
    white-space: nowrap;
  }
  .brand__dot {
    display: inline-block;
    width: 8px; height: 8px;
    border-radius: 50%;
    background: var(--accent);
  }
  .card--front .brand {
    right: 36px;
    top: 126px;
    font-size: 36px;
  }
  .card--back .brand {
    left: 0; right: 0;
    justify-content: center;
    top: 150px;
    font-size: 42px;
  }
  .person {
    position: absolute;
    left: 33px;
    top: 194px;
    right: 36px;
  }
  .person__name {
    font-family: "Montserrat", Arial, sans-serif;
    font-weight: 700;
    font-size: 23px;
    line-height: 1;
    color: var(--accent);
    letter-spacing: 0.2px;
  }
  .person__role {
    display: flex;
    align-items: center;
    gap: 8px;
    margin-top: 4px;
    font-size: 16px;
  }
  .person__role::after {
    content: "";
    flex: 1;
    height: 1px;
    background: var(--rule);
    margin-top: 3px;
  }
  .contact {
    position: absolute;
    left: 33px;
    top: 264px;
    list-style: none;
    font-size: 16px;
    line-height: 21px;
  }
  .contact__item { display: flex; align-items: center; gap: 5px; white-space: nowrap; }
  .contact__icon { width: 15px; height: 15px; flex: none; }
  .contact__highlight { color: var(--accent); }
  .address {
    position: absolute;
    right: 36px;
    top: 283px;
    text-align: right;
    font-style: normal;
    font-size: 16px;
    line-height: 21px;
    white-space: nowrap;
  }
</style>
</head>
<body>
  <section class="card card--front" aria-label="Business card front">
    <div class="brand">VR HOLDINGS<span class="brand__dot"></span></div>

    <div class="person">
      <h1 class="person__name">MORGAN REYES</h1>
      <p class="person__role">Managing Director</p>
    </div>

    <ul class="contact">
      <li class="contact__item">
        <svg class="contact__icon" viewBox="0 0 16 16" aria-hidden="true">
          <path d="M4 1.5 6 4.5 4.6 6.2c.9 2 2.3 3.4 4.2 4.3L10.5 9l3 2-1.2 2.6C7 13.3 2.7 9 2.4 3.2Z" fill="none" stroke="#e8391f" stroke-width="1.6" stroke-linejoin="round"/>
          <path d="M9.5 1.8a5 5 0 0 1 4.7 4.7M9.3 4.2a2.6 2.6 0 0 1 2.5 2.5" fill="none" stroke="#e8391f" stroke-width="1.3"/>
        </svg>
        <span>073-555 018 462</span>
      </li>
      <li class="contact__item">
        <svg class="contact__icon" viewBox="0 0 16 16" aria-hidden="true">
          <rect x="0.5" y="3" width="15" height="10" fill="#e8391f"/>
          <path d="M0.5 3 8 9l7.5-6M0.5 13l5.2-5M15.5 13l-5.2-5" fill="none" stroke="#000" stroke-width="1"/>
        </svg>
        <span>morgan@vrholdingsgroup.example</span>
      </li>
      <li class="contact__item">
        <svg class="contact__icon" viewBox="0 0 16 16" aria-hidden="true">
          <g fill="none" stroke="#e8391f" stroke-width="1.3">
            <circle cx="8" cy="8" r="6.8"/>
            <ellipse cx="8" cy="8" rx="3" ry="6.8"/>
            <path d="M1.2 8h13.6M2.3 4.5h11.4M2.3 11.5h11.4M8 1.2v13.6"/>
          </g>
        </svg>
        <span>www.<span class="contact__highlight">vrholdingsgroup</span>.example</span>
      </li>
    </ul>

    <address class="address">
      88, Quarry Lane Works<br>
      2150, Australia
    </address>

    <div class="card__band"></div>
  </section>

  <section class="card card--back" aria-label="Business card back">
    <div class="brand">VR HOLDINGS<span class="brand__dot"></span></div>
    <div class="card__band"></div>
  </section>
</body>
</html>
```